Defend science flier

Put my name and text below on one side of flier, and place other text on other side. Try to keep file about 4 by 6 or 6 by 8 inches.

Target Market(s)

Community and retailers.

Industry/Entity Type

Retail and concerned community.

Font styles to use
Serif

Requirements
Must have
• Good, eye-catching titles. Be smaller format. Not 8 by 11
Nice to have
• Black and white text. Maybe bullets etc for organizion but no decorations.
Should not have
• Any decoration

```html
<!DOCTYPE html>
<html lang="en">
<head>
<meta charset="utf-8">
<title>Defend Science Flier</title>
<link href="https://fonts.googleapis.com/css2?family=Libre+Baskerville:ital,wght@0,400;0,700;1,400&family=Crimson+Text:ital,wght@0,400;0,600;0,700;1,400&display=swap" rel="stylesheet">
<style>
  :root {
    --gold: #b8963e;
    --gold-dark: #8f7128;
    --cream: #f8f3e4;
    --ink: #1f1a14;
    --ink-soft: #3a332a;
    --page: #ecebe7;
    --white: #ffffff;
  }
  * { box-sizing: border-box; margin: 0; padding: 0; }
  html, body {
    width: 784px; height: 1200px; overflow: hidden;
    background: var(--page);
  }
  .flier {
    position: absolute; top: 322px;
    width: 364px; height: 556px;
    background: var(--gold);
    padding: 12px;
    box-shadow: 0 2px 8px rgba(0,0,0,0.15);
  }
  .flier--front { left: 18px; }
  .flier--back { left: 402px; }
  .flier__inner {
    height: 100%;
    background: var(--cream);
    border: 1px solid var(--gold-dark);
    display: flex; flex-direction: column;
    color: var(--ink);
    font-family: "Crimson Text", serif;
    text-align: center;
  }
  /* Front */
  .front__head { padding: 28px 4px 14px; border-bottom: 1px solid var(--gold); margin: 0 14px; }
  .author-name {
    font-family: "Libre Baskerville", serif; font-weight: 700;
    font-size: 20px; letter-spacing: -0.3px; white-space: nowrap;
  }
  .author-tagline {
    font-family: "Libre Baskerville", serif; font-style: italic;
    font-size: 10px; margin-top: 6px; color: var(--ink-soft); white-space: nowrap;
  }
  .front__body { padding: 16px 30px 0; }
  .front__body p { font-size: 12px; line-height: 1.35; margin-bottom: 11px; }
  .quote-mark {
    font-family: "Libre Baskerville", serif; font-weight: 700;
    color: var(--gold); font-size: 64px; line-height: 0.7; margin-top: 8px; height: 34px;
  }
  .endorsement {
    font-weight: 700; font-size: 13px; line-height: 1.3;
    padding: 6px 26px 0;
  }
  .front__foot { margin-top: auto; }
  .more-details { font-size: 11px; font-weight: 600; margin-bottom: 6px; }
  .site-band {
    background: var(--gold); color: var(--white);
    font-family: "Libre Baskerville", serif; font-weight: 700;
    font-size: 15px; letter-spacing: 0.5px; padding: 9px 0;
  }
  /* Back */
  .flier--back .flier__inner { text-align: left; padding: 24px 22px; }
  .back__title {
    font-family: "Libre Baskerville", serif; font-weight: 700;
    font-size: 21px; line-height: 1.2; text-align: center;
  }
  .back__lead {
    font-size: 13px; font-weight: 600; text-align: center;
    line-height: 1.3; margin: 8px 0 14px;
  }
  .sin-list {
    list-style: none; display: grid; grid-template-columns: 1fr 1fr;
    grid-auto-flow: column; grid-template-rows: repeat(4, auto);
    column-gap: 14px; row-gap: 9px;
    border-top: 1px solid var(--gold); border-bottom: 1px solid var(--gold);
    padding: 12px 0;
  }
  .sin-list li { font-size: 11px; line-height: 1.25; padding-left: 12px; position: relative; }
  .sin-list li::before {
    content: ""; position: absolute; left: 0; top: 4px;
    width: 6px; height: 6px; background: var(--gold);
  }
  .sin-list b { font-weight: 700; }
  .back__text p { font-size: 11.5px; line-height: 1.38; margin-top: 12px; text-align: center; }
</style>
</head>
<body>

<section class="flier flier--front">
  <div class="flier__inner">
    <header class="front__head">
      <h1 class="author-name">Martin R. Keller, Ph.D.</h1>
      <p class="author-tagline">"The Newton and Einstein of Psychology and History"</p>
    </header>
    <div class="front__body">
      <p>Martin's Bio-Psych has Restructured the Liberal Arts and Sciences—from Genetics to the Fine Arts and Hollywood</p>
      <p>Museum Catalogues, Better Nutrition, and Hollywood Films Now Use Martin's Methods</p>
      <p>Martin's Biopsych is endorsed by Dr. L. Warren Haskell, professor of psychiatry at Northbrook Medical School, who said:</p>
    </div>
    <div class="quote-mark">“</div>
    <p class="endorsement">Modern sleep and dream research teaches us—as does Martin Keller's book <i>The Brain Behind Belief</i>—that all human activities, including art and politics, are products of the human brain, and that each of us has the privilege and responsibility of using it and communicating its creations.</p>
    <footer class="front__foot">
      <p class="more-details">Martin's homepage for more details</p>
      <div class="site-band">www.martin-keller.org</div>
    </footer>
  </div>
</section>

<section class="flier flier--back">
  <div class="flier__inner">
    <h2 class="back__title">WHY DID THE CULTURE CHANGE?</h2>
    <p class="back__lead">During the 1960s, we socialized the Seven Deadly Sins. Therefore:</p>
    <ul class="sin-list">
      <li><b>Pride</b> became "Racism"</li>
      <li><b>Lust</b> became "Sexism" and "Gender"</li>
      <li><b>Gluttony</b> became "Consumer Fatness"</li>
      <li><b>Sloth</b> became "The lack of social action"</li>
      <li><b>Vanity</b> became "Media images of beauty"</li>
      <li><b>Envy</b> became "Inequality"</li>
      <li><b>Wrath</b> became "Protest"</li>
    </ul>
    <div class="back__text">
      <p>This "fight for diversity" inspires attacks against people like Dr. Keller for asserting any reality principle about human nature.</p>
      <p>These moral and religious crusaders only ignore the role of sin and try to slow the progress of science. They label anyone who disagrees a "bad" person.</p>
      <p>The educational and cultural elites, such as Hollywood, now reject these older moral ideas. The elites are replacing them with new political sins.</p>
    </div>
  </div>
</section>

</body>
</html>
```